2 Page Business Flyer for Finance Business

Need a two page flyer created for a finance business. Lots of text and needs to fit on two pages.

Corporate business/banking look and feel. Not too many large images. Lots of white space, clean design. Attached is color palette and the text contents of the flyer.

```html
<!DOCTYPE html>
<html lang="en">
<head>
<meta charset="utf-8">
<title>Vanilla Option – Two Page Flyer</title>
<link href="https://fonts.googleapis.com/css2?family=Quicksand:wght@400;500;600;700&display=swap" rel="stylesheet">
<style>
  :root{
    --navy:#2f2e57;
    --navy-deep:#262548;
    --green:#5cc48a;
    --teal:#3db9a3;
    --red:#c8473d;
    --text:#4a4a5a;
    --stage:#dfe0e2;
    --white:#ffffff;
  }
  *{box-sizing:border-box;margin:0;padding:0}
  html,body{width:1200px;height:821px;overflow:hidden;background:var(--stage);font-family:"Quicksand",sans-serif;color:var(--text)}
  .page{position:absolute;top:72px;width:508px;height:677px;background:var(--white);overflow:hidden}
  .page--front{left:71px}
  .page--back{left:621px}
  .abs{position:absolute}
  .body-copy{font-size:6.6px;line-height:10px;font-weight:500}
  .body-copy p+p,.body-copy p+ul,.body-copy ul+p{margin-top:10px}
  .bullets{list-style:none}
  .bullets li{position:relative;padding-left:11px}
  .bullets li::before{content:"";position:absolute;left:1px;top:4px;width:3px;height:3px;border-radius:50%;background:var(--teal)}
  .section-title{font-size:14.5px;line-height:17px;font-weight:500;color:var(--teal)}
  .section-title strong{font-weight:700}
  .rule{position:absolute;width:36px;height:2px;background:var(--red)}
  .accent{color:var(--red);font-weight:600}
  .doc-title{font-weight:700;color:var(--white);letter-spacing:.3px}
  .site{font-size:8.5px;font-weight:600;color:var(--teal)}
  .brand{display:flex;align-items:center;gap:6px;font-size:17px;font-weight:700;letter-spacing:1px}
  .brand-mark{width:18px;height:18px;border-radius:3px;background:var(--teal)}
  .feature-icon{position:absolute;width:58px;height:58px;border-radius:50%;background:var(--navy);border:2px solid var(--green);left:77px}
  .feature-title{font-size:12px;font-weight:700;color:var(--red)}
  .divider{position:absolute;left:123px;width:276px;border-top:1px dashed #b9b9c6}
</style>
</head>
<body>

<!-- Front page -->
<section class="page page--front">
  <div class="abs" style="left:0;top:0;width:508px;height:160px" role="img" aria-label="Business handshake photograph in navy tones behind the title"></div>
  <svg class="abs" style="left:0;top:0" width="508" height="160" viewBox="0 0 508 160">
    <defs>
      <linearGradient id="heroTone" x1="0" y1="0" x2="1" y2="1">
        <stop offset="0" stop-color="#3a3a68"/><stop offset="1" stop-color="#2b2a52"/>
      </linearGradient>
    </defs>
    <path d="M0 0H508V62C430 130 300 158 190 150C110 144 45 110 0 76Z" fill="var(--green)"/>
    <path d="M0 0H508V58C430 124 300 150 190 142C110 136 45 100 0 60Z" fill="url(#heroTone)"/>
    <path d="M0 82C50 122 120 150 200 154C300 160 430 130 508 70" fill="none" stroke="var(--green)" stroke-width="1"/>
  </svg>
  <h1 class="abs doc-title" style="left:0;width:508px;top:44px;text-align:center;font-size:40px">Vanilla Option</h1>

  <h2 class="abs section-title" style="left:34px;top:182px;width:200px">How does a <strong>Vanilla Option</strong> contract work?</h2>
  <span class="rule" style="left:34px;top:229px"></span>
  <div class="abs body-copy" style="left:34px;top:245px;width:203px">
    <p>The buyer of a vanilla option receives protection against an adverse movement in the exchange rate while allowing full participation in a beneficial move. At no time is the buyer of a Vanilla Option obligated to exercise the Option and transact the currencies, therefore providing flexibility in cases where the requirement to purchase foreign currency is not certain.</p>
    <p>A buyer of vanilla options is required to pay a premium (like an insurance premium) for the right, but not the obligation, to exchange currency at a predetermined rate on a predetermined date.</p>
    <ul class="bullets">
      <li>Set a protection rate which will be your worst-case scenario at expiry.</li>
      <li>Determine the amount of currency you wish to protect.</li>
      <li>Choose an expiry date for the contract.</li>
      <li>Calculate the premium you are required to pay.</li>
    </ul>
  </div>

  <div class="abs section-title" style="left:268px;top:182px;font-size:12.5px">Let's look at an example:</div>
  <h2 class="abs section-title" style="left:268px;top:196px;font-size:18px;line-height:22px"><strong>You are in importer.</strong></h2>
  <span class="rule" style="left:268px;top:229px"></span>

  <!-- lower navy band -->
  <div class="abs" style="left:0;top:446px;width:508px;height:215px;background:var(--navy)"></div>
  <div class="abs" style="left:0;top:661px;width:97px;height:16px;background:var(--teal)"></div>
  <div class="abs" style="left:97px;top:661px;width:411px;height:16px;background:var(--red)"></div>
  <div class="abs" style="left:246px;top:240px;width:248px;height:356px;background:var(--white)"></div>

  <div class="abs body-copy" style="left:268px;top:245px;width:206px">
    <p>Your construction company has bid on a project that if successful, will require you to import materials from the United States to use in construction. You have used todays pricing of materials in calculating your bid and want to protect against an adverse move in the US dollar exchange rate from eroding your margin if your bid is chosen for the project.</p>
    <p>You choose to buy a Vanilla Call which will protect you from a rise in the USD/CAD exchange rate above your protection rate. You choose to buy protection on $500,000 USD, with a protection rate (strike rate) of 1.3300 expiring 3 months from now. You are required to pay a premium which in this case is calculated to be 1.8%, or 11,970 CAD.</p>
    <p><span class="accent">Your bid is successful:</span> If the exchange rate is below your protection rate at expiration, you have no obligation relating to the vanilla call and you are free to buy USD at the cheaper spot rate. If the exchange rate is above your protection rate, your have the right to purchase your USD at the protection rate, and thereby claiming your insurance policy.</p>
    <p><span class="accent">Your bid is not successful:</span> You have no obligation relating to the vanilla option however, if at expiry the exchange rate is above the protection rate, you may exercise your right to buy USD at the lower rate and simultaneous sell USD back at the prevailing spot rate, thereby recouping some or all of the premium paid to buy the option.</p>
    <p>Alternatively, if you find out your bid was not successful with time still left until expiration, you may sell your option back into the market in the case that it still has residual value, which will depend on various market factors.</p>
  </div>

  <h2 class="abs section-title" style="left:34px;top:478px;font-weight:400">Why use<br><strong>Vanilla Options?</strong></h2>
  <svg class="abs" style="left:165px;top:476px" width="48" height="48" viewBox="0 0 48 48" fill="none" stroke="#6a6a8e" stroke-width="1.3">
    <rect x="6" y="4" width="28" height="16" rx="1" transform="rotate(-8 20 12)"/>
    <rect x="2" y="12" width="30" height="18" rx="1"/>
    <circle cx="17" cy="21" r="5"/>
    <ellipse cx="38" cy="24" rx="8" ry="3"/>
    <path d="M30 24v16c0 2 16 2 16 0V24M30 29c0 2 16 2 16 0M30 34c0 2 16 2 16 0"/>
  </svg>
  <span class="rule" style="left:34px;top:524px"></span>
  <div class="abs body-copy" style="left:36px;top:540px;width:180px;color:#e6e6ef">
    <p>Vanilla options are often compared to an insurance product. The buyer pays a non-refundable premium for the right, but not the obligation to trade currency in the future at the protection rate of the option. This product allows you to participate in a beneficial move to an unlimited extent, which will be the most advantageous outcome, if the exchange rate moves in your favour enough to more than offset the premium paid for the option.</p>
  </div>

  <div class="abs site" style="left:269px;top:628px">NorvaLink.com</div>
  <div class="abs brand" style="left:391px;top:622px;color:var(--white)"><span class="brand-mark"></span>NORVA</div>
</section>

<!-- Back page -->
<section class="page page--back">
  <div class="abs" style="left:0;top:0;width:106px;height:370px;background:var(--navy)"></div>
  <div class="abs" style="left:0;top:370px;width:37px;height:307px;background:var(--navy)"></div>
  <svg class="abs" style="left:200px;top:0" width="308" height="112" viewBox="0 0 308 112">
    <path d="M0 0H308V112C200 112 80 80 0 0Z" fill="var(--green)"/>
    <path d="M10 0H308V104C200 104 90 70 10 0Z" fill="var(--navy)"/>
  </svg>
  <h1 class="abs doc-title" style="left:320px;top:38px;font-size:24px">Vanilla Option</h1>

  <div class="feature-icon" style="top:95px"><svg width="54" height="54" viewBox="0 0 54 54" fill="none" stroke="#fff" stroke-width="1.3"><rect x="17" y="13" width="20" height="27" rx="2"/><circle cx="27" cy="22" r="4"/><path d="M21 31h12M21 35h12"/></svg></div>
  <div class="feature-icon" style="top:191px"><svg width="54" height="54" viewBox="0 0 54 54" fill="none" stroke="#fff" stroke-width="1.3"><path d="M36 16c-8 1-14 7-17 15l4 4c8-3 14-9 15-17z"/><circle cx="30" cy="24" r="2"/><path d="M20 34l-5 5M19 28l-5 1 4-5M26 35l-1 5 5-4"/></svg></div>
  <div class="feature-icon" style="top:281px"><svg width="54" height="54" viewBox="0 0 54 54" fill="none" stroke="#fff" stroke-width="1.3"><rect x="17" y="17" width="20" height="20" transform="rotate(45 27 27)"/><path d="M27 20v9"/><circle cx="27" cy="33" r="1" fill="#fff"/></svg></div>

  <div class="abs feature-title" style="left:150px;top:94px">Characteristics</div>
  <ul class="abs bullets body-copy" style="left:150px;top:117px;width:260px">
    <li>You are looking for a straight-forward hedging solution</li>
    <li>You want to receive full benefit from an appreciation of the currency you are exposed to</li>
    <li>You are comfortable receiving protection at the strike rate of the option</li>
    <li>You are willing to pay the non-refundable premium</li>
  </ul>
  <div class="divider" style="top:180px"></div>

  <div class="abs feature-title" style="left:150px;top:195px">Advantages</div>
  <ul class="abs bullets body-copy" style="left:150px;top:218px;width:270px">
    <li>You hedge your foreign currency exposure at a predefined hedge rate</li>
    <li>You can choose the hedge rate that suits your budget requirements</li>
    <li>Provides the ability to fully participate in a favourable exchange rate move</li>
    <li>You can choose from most major currency pairs to meet your needs</li>
  </ul>
  <div class="divider" style="top:273px"></div>

  <div class="abs feature-title" style="left:150px;top:287px">Risks</div>
  <div class="abs body-copy" style="left:150px;top:310px;width:250px">Premium paid is non-refundable and remains your only obligation when buying vanilla options</div>

  <h2 class="abs section-title" style="left:60px;top:393px;font-size:14px">What <strong>determines the price</strong> of a Vanilla Option?</h2>
  <div class="abs body-copy" style="left:60px;top:442px;width:372px">
    <p>The cost of an option is defined by the premium that is required to be paid in order to enter into the contract. Premiums are calculated using the industry standard formulas based upon the Black Scholes model. The most important variables in the option pricing formulas include the following:</p>
    <ul class="bullets">
      <li>The current market Spot Rate.</li>
      <li>Market volatility – the higher the volatility, the higher the premium.</li>
      <li>The Term of the Option – a longer term typically results in a higher premium.</li>
      <li>The Strike Rate – the closer to being ITM the protection rate is, the higher the premium.</li>
      <li>The interest rate differential of the two currencies involved.</li>
      <li>Style – European or American, or whether the option can be exercised prior to expiration</li>
    </ul>
    <p>An option can either a European (meaning that they can only be exercised on the expiry date), or American (meaning that they can be exercised at any time prior to expiration). We normally deals in European options however, we do offer American options under certain circumstances and when specific delivery terms are agreed upon between us and the customer.</p>
  </div>

  <div class="abs site" style="left:128px;top:629px">NorvaLink.com</div>
  <div class="abs brand" style="left:385px;top:623px;color:var(--navy)"><span class="brand-mark"></span>NORVA</div>
</section>

</body>
</html>
```